***Design a Nutritional Supplement Label for Bright Harvest!***

I have an existing label, I want to keep the logo but change the rest of the design. I am open to different creative ideas, but it needs to look appropriate for the shelves at Bright Harvest. This means it needs to look professional and premium, without being sterile and boring. I feel like my current label looks a little 1990s. You can play with the colors, font and design elements, while keeping the logo, descriptive text and the same layout. Feel free to take some bold chances. (You cannot change the font in the supplement facts section)

Font styles to use
Sans Serif

Colors

Designer to choose colors to be used in the design.

Requirements
Must have
• Keep the same text and layout. Keep the "Muscle Haven" logo as-is. DO NOT CHANGE THE LOGO!!

```html
<!DOCTYPE html>
<html lang="en">
<head>
<meta charset="utf-8">
<title>Muscle Haven — Supplement Label</title>
<link rel="stylesheet" href="https://fonts.googleapis.com/css2?family=Bebas+Neue&family=Oswald:wght@400;500&family=Montserrat:wght@500&display=swap">
<style>
  :root {
    --page: #ffffff;
    --label-white: #fbfbfb;
    --label-shade: #e9e9e9;
    --lime: #a9c63c;
    --lime-light: #b8d24e;
    --ink: #1b1b1b;
    --ink-soft: #3b3b3b;
    --logo: #ffffff;
    --tag: #eef3d2;
  }
  * { margin: 0; padding: 0; box-sizing: border-box; }
  html, body {
    width: 1200px;
    height: 1200px;
    overflow: hidden;
    background: var(--page);
  }
  .canvas {
    position: relative;
    width: 1200px;
    height: 1200px;
  }
  .label {
    position: absolute;
    left: 50px;
    top: 200px;
    width: 1100px;
    height: 800px;
    background: linear-gradient(90deg, var(--label-shade) 0%, var(--label-white) 22%, var(--label-white) 100%);
    overflow: hidden;
  }
  .label-panel {
    position: absolute;
    inset: 0;
    width: 1100px;
    height: 800px;
  }
  .brand {
    position: absolute;
    left: 570px;
    top: 60px;
    width: 340px;
    text-align: center;
    color: var(--logo);
    font-family: "Montserrat", sans-serif;
    font-weight: 500;
  }
  .brand-line-top {
    display: block;
    font-size: 64px;
    line-height: 1;
    letter-spacing: 2px;
  }
  .brand-line-bottom {
    display: block;
    font-size: 26px;
    line-height: 1;
    margin-top: 12px;
    letter-spacing: 12px;
    padding-left: 12px;
  }
  .claims {
    position: absolute;
    left: 114px;
    top: 355px;
    font-family: "Bebas Neue", "Oswald", sans-serif;
    color: var(--ink);
    line-height: 1;
  }
  .claim { display: block; }
  .claim-high { font-size: 112px; letter-spacing: 1px; }
  .claim-absorption { font-size: 62px; margin-top: 16px; letter-spacing: 1px; }
  .claim-fast { font-size: 122px; margin-top: 8px; letter-spacing: 1px; }
  .claim-acting { font-size: 74px; margin-top: 20px; letter-spacing: 1px; }
  .count-tag {
    position: absolute;
    left: 720px;
    top: 546px;
    width: 104px;
    height: 70px;
    background: var(--tag);
    border-radius: 4px;
    font-family: "Oswald", sans-serif;
    font-weight: 400;
    font-size: 20px;
    line-height: 1.3;
    color: var(--ink-soft);
    text-align: center;
    padding-top: 8px;
  }
  .product-type {
    position: absolute;
    left: 580px;
    top: 722px;
    font-family: "Oswald", sans-serif;
    font-weight: 400;
    font-size: 27px;
    letter-spacing: 2px;
    color: var(--ink-soft);
  }
</style>
</head>
<body>
  <main class="canvas">
    <section class="label">
      <svg class="label-panel" viewBox="0 0 1100 800" aria-hidden="true">
        <defs>
          <linearGradient id="limeFill" x1="0" y1="0" x2="1" y2="1">
            <stop offset="0" stop-color="#b8d24e"/>
            <stop offset="1" stop-color="#a4c137"/>
          </linearGradient>
        </defs>
        <polygon points="569,0 1100,0 1100,800 240,800" fill="url(#limeFill)"/>
      </svg>

      <div class="brand">
        <span class="brand-line-top">MUSCLE</span>
        <span class="brand-line-bottom">HAVEN</span>
      </div>

      <h1 class="claims">
        <span class="claim claim-high">High</span>
        <span class="claim claim-absorption">Absorption</span>
        <span class="claim claim-fast">Fast</span>
        <span class="claim claim-acting">Acting</span>
      </h1>

      <div class="count-tag">180<br>Capsules</div>
      <p class="product-type">DIETARY SUPPLEMENT</p>
    </section>
  </main>
</body>
</html>
```